Awesome, colorful pamphlet advertising services for disabled people and supporters

My business, The Wellness Crossroads, provides nutritional counseling services to people with and without disabilities throughout the lifespan. It also offers disability consulting, body image coaching and accessible recreation consultation. I would like something representing both children and adults which ties these activities together in a happy way.

Font styles to use
Sans Serif

Colors
00AB8E
00BBA5
67D7C9
C6EFE9
E9F9F6
FFF300
FFF600
FEFA6F
FFFEC7
FFFEE8
F0912C
F2A743
F7CA91
FBE8D2
FDF5EE
E54698
E96AAD
F1A4CE
F9D9EA
FCEFF6
6B429C
8869AF
B7A5CE
E3DAEB
F3F0F8

```html
<!DOCTYPE html>
<html lang="en">
<head>
<meta charset="utf-8">
<title>The Wellness Crossroads – Brochure</title>
<link href="https://fonts.googleapis.com/css2?family=Asap+Condensed:ital,wght@0,600;0,700;0,800;1,500&family=Poppins:ital,wght@0,400;0,500;0,600;0,700;1,400&display=swap" rel="stylesheet">
<style>
  :root{
    --green-deep:#17765f;
    --green:#1f8a70;
    --teal:#3bb79d;
    --teal-soft:#67d7c9;
    --mint:#e9f9f6;
    --orange:#e8692a;
    --purple:#6b429c;
    --purple-soft:#8869af;
    --pink:#e54698;
    --white:#ffffff;
    --ink:#1e5e4f;
    --stage:#ece7df;
    --head:"Asap Condensed", "Arial Narrow", sans-serif;
    --body:"Poppins", Arial, sans-serif;
  }
  *{box-sizing:border-box;margin:0;padding:0}
  html,body{width:1200px;height:900px;overflow:hidden;background:var(--stage)}
  body{position:relative;font-family:var(--body);color:var(--ink)}
  .spread{position:absolute;top:245px;width:580px;height:410px;display:flex;background:var(--white);box-shadow:0 2px 10px rgba(0,0,0,.12)}
  .spread--outer{left:10px}
  .spread--inner{left:610px}
  .page{position:relative;width:290px;height:410px;overflow:hidden}
  .page + .page{border-left:1px solid rgba(0,0,0,.06)}
  .fill{position:absolute}
  .waves{position:absolute;left:0;top:0;width:290px;height:410px}

  /* back cover */
  .photo-rehab{left:0;top:0;width:290px;height:260px;background:linear-gradient(135deg,#2f5f7e 0%,#6b8aa0 40%,#b9a48a 75%,#8a6a4d 100%)}
  .contact{position:absolute;left:22px;top:282px;color:var(--white)}
  .contact__title{font-family:var(--head);font-weight:700;font-size:17px;letter-spacing:.2px}
  .contact__lead{font-style:italic;font-size:9px;margin-bottom:12px}
  .contact__row{display:flex;align-items:center;gap:8px;font-size:8.6px;margin-bottom:9px}
  .contact__icon{width:15px;height:15px;border-radius:50%;background:var(--white);display:flex;align-items:center;justify-content:center}

  /* front cover */
  .photo-play{left:70px;top:0;width:220px;height:270px;background:linear-gradient(160deg,#4f8a3a 0%,#7bb05a 45%,#c7864a 70%,#6c4a7a 100%)}
  .brand-tab{position:absolute;left:14px;top:-6px;width:100px;height:116px;background:var(--white);border:4px solid var(--green);border-top:none;border-radius:0 0 50px 50px;display:flex;flex-direction:column;align-items:center;justify-content:center;gap:6px;padding-top:10px}
  .brand-tab__dot{width:18px;height:18px;border-radius:50%;background:var(--purple)}
  .brand-tab__name{font-family:var(--body);font-weight:600;font-size:8.5px;line-height:1.15;text-align:center;color:var(--purple)}
  .label-tab{position:absolute;right:0;top:22px;background:var(--green);color:var(--white);font-size:7.5px;font-weight:600;padding:8px 10px 8px 14px}
  .welcome{position:absolute;left:8px;top:140px;width:180px;height:180px;border-radius:50%;background:var(--green);color:var(--white);text-align:center;display:flex;flex-direction:column;justify-content:center;padding:0 18px}
  .welcome__title{font-family:var(--head);font-weight:800;font-size:17px;line-height:1.05;text-transform:uppercase;margin-bottom:6px}
  .welcome__text{font-size:6.8px;line-height:1.35}
  .call-now{position:absolute;left:185px;top:238px;width:76px;height:76px;border-radius:50%;background:var(--orange);color:var(--white);font-family:var(--head);font-weight:800;font-size:19px;line-height:.95;text-align:center;display:flex;align-items:center;justify-content:center}
  .tagline{position:absolute;left:0;right:0;top:368px;text-align:center;color:var(--white);font-family:var(--head);font-weight:700;font-size:11.5px;letter-spacing:.2px}

  /* services page */
  .section-title{position:absolute;font-family:var(--head);font-weight:800;color:var(--green);text-transform:uppercase;line-height:1}
  .services-title{left:28px;top:40px;font-size:22px}
  .service{position:absolute;width:116px;height:40px;background:var(--green);border-radius:4px;color:var(--white);font-family:var(--head);font-weight:700;font-size:6.8px;line-height:1.15;text-transform:uppercase;display:flex;align-items:center;padding:0 8px 0 18px}
  .service__num{position:absolute;left:-7px;top:6px;width:15px;height:15px;border-radius:50%;background:var(--white);border:2px solid var(--teal);color:var(--green);font-size:6px;display:flex;align-items:center;justify-content:center}
  .profile-photo{position:absolute;left:168px;top:230px;width:78px;height:78px;border-radius:50%;border:4px solid var(--green);background:radial-gradient(circle at 50% 40%,#c9a58e 0%,#8b6b58 60%,#3f4a45 100%)}
  .profile{position:absolute;left:18px;top:272px;width:260px;color:var(--white)}
  .profile__name{font-family:var(--head);font-weight:700;font-size:14px;line-height:1.1}
  .profile__quote{font-style:italic;font-size:9px;margin:6px 0 5px}
  .profile__bio{font-size:5.6px;line-height:1.4;width:230px}

  /* why page */
  .why-title{left:22px;top:40px;font-size:20px}
  .why-text{position:absolute;left:22px;top:66px;width:248px;font-size:6.4px;line-height:1.35;color:var(--green)}
  .photo-area{position:absolute;left:0;top:0;width:290px;height:410px}
  .badge{position:absolute;border-radius:50%}
  .badge--purple{left:14px;top:168px;width:76px;height:76px;background:var(--purple-soft);border:4px solid var(--white);box-shadow:0 0 0 2px var(--purple)}
  .badge--grey{left:222px;top:158px;width:60px;height:60px;background:var(--white);border:5px solid #b7a5ce}
  .badge--pink{left:14px;top:318px;width:62px;height:62px;background:var(--white);border:5px solid var(--pink)}
</style>
</head>
<body>

<!-- Outer spread: back cover + front cover -->
<section class="spread spread--outer">
  <article class="page page--back">
    <div class="fill photo-rehab" role="img" aria-label="Photo of an older man in a wheelchair doing stretching exercises with a band at home"></div>
    <svg class="waves" viewBox="0 0 290 410" aria-hidden="true">
      <path d="M0 215 C70 190 150 215 290 255 L290 410 L0 410 Z" fill="#3bb79d"/>
      <path d="M0 240 C80 225 170 250 290 300 L290 410 L0 410 Z" fill="#1f8a70"/>
    </svg>
    <div class="contact">
      <h2 class="contact__title">GET IN TOUCH</h2>
      <p class="contact__lead">Please call us for more information.</p>
      <p class="contact__row"><span class="contact__icon"><svg width="9" height="9" viewBox="0 0 24 24"><path d="M6.6 10.8a15 15 0 0 0 6.6 6.6l2.2-2.2c.3-.3.7-.4 1-.2 1.1.4 2.3.6 3.6.6.6 0 1 .4 1 1V20c0 .6-.4 1-1 1C10.6 21 3 13.4 3 4c0-.6.4-1 1-1h3.5c.6 0 1 .4 1 1 0 1.3.2 2.5.6 3.6.1.3 0 .7-.2 1z" fill="#1f8a70"/></svg></span>(555) 014-2290</p>
      <p class="contact__row"><span class="contact__icon"><svg width="9" height="9" viewBox="0 0 24 24"><path d="M3 5h18v14H3z" fill="#1f8a70"/><path d="M3 5l9 7 9-7" stroke="#fff" stroke-width="2" fill="none"/></svg></span>hello@wellnesscrossroads.example</p>
      <p class="contact__row"><span class="contact__icon"><svg width="9" height="9" viewBox="0 0 24 24"><circle cx="12" cy="12" r="9" stroke="#1f8a70" stroke-width="2" fill="none"/><path d="M3 12h18M12 3c3 3 3 15 0 18M12 3c-3 3-3 15 0 18" stroke="#1f8a70" stroke-width="1.6" fill="none"/></svg></span>www.wellnesscrossroads.example</p>
    </div>
  </article>

  <article class="page page--front">
    <div class="fill photo-play" role="img" aria-label="Photo of a smiling girl in a wheelchair holding a basketball outdoors"></div>
    <div class="brand-tab">
      <span class="brand-tab__dot"></span>
      <span class="brand-tab__name">The Wellness<br>Crossroads</span>
    </div>
    <div class="label-tab">Wellness Crossroads</div>
    <svg class="waves" viewBox="0 0 290 410" aria-hidden="true">
      <path d="M0 290 C90 320 190 300 290 250 L290 410 L0 410 Z" fill="#3bb79d"/>
      <path d="M0 320 C100 345 200 325 290 290 L290 410 L0 410 Z" fill="#1f8a70"/>
    </svg>
    <div class="welcome">
      <h1 class="welcome__title">Welcome to<br>The Wellness<br>Crossroads</h1>
      <p class="welcome__text">We provide nutritional counseling services to people with and without disabilities throughout the lifespan. We also offer disability consulting, body image coaching and accessible recreation consultation</p>
    </div>
    <div class="call-now">CALL<br>NOW</div>
    <p class="tagline">ELEVATE, ENCOURAGE, ESTEEM, EDUCATE</p>
  </article>
</section>

<!-- Inner spread: services + why choose us -->
<section class="spread spread--inner">
  <article class="page page--services">
    <h2 class="section-title services-title">Our Service</h2>
    <div class="service" style="left:24px;top:80px"><span class="service__num">01</span>Self and body esteem as related to disability</div>
    <div class="service" style="left:24px;top:128px"><span class="service__num">02</span>Trauma and healing with a disability</div>
    <div class="service" style="left:24px;top:176px"><span class="service__num">03</span>Early childhood support for disabled children and care providers</div>
    <div class="service" style="left:152px;top:90px"><span class="service__num">04</span>Movement as fun for disabled kids and adults</div>
    <div class="service" style="left:152px;top:138px"><span class="service__num">05</span>Accessible recreation/play consults</div>
    <div class="service" style="left:152px;top:186px"><span class="service__num">06</span>Moving away from therapies / assessing therapy from a disability positive perspective</div>
    <svg class="waves" viewBox="0 0 290 410" aria-hidden="true">
      <path d="M0 250 C60 225 140 235 290 285 L290 410 L0 410 Z" fill="#3bb79d"/>
      <path d="M0 268 C80 255 170 275 290 320 L290 410 L0 410 Z" fill="#1f8a70"/>
    </svg>
    <div class="profile-photo" role="img" aria-label="Portrait photo of the counselor"></div>
    <div class="profile">
      <h3 class="profile__name">DANA WHITFIELD<br>(MSW, FNLP, CARSS 1)</h3>
      <p class="profile__quote">I will always provide my best service.</p>
      <p class="profile__bio">I am a non-clinical (macro) social worker specializing in disability issues. I provide disability positive consulting (not therapy) to parents/guardians, therapists and others working to help the disability community and am available for consultation virtually.</p>
    </div>
  </article>

  <article class="page page--why">
    <h2 class="section-title why-title">Why Choose Us !</h2>
    <p class="why-text">This is a place of safety, encouragement and evidence-based practices. Using macro social work skills and personal experience with physical, learning disability and chronic illness, The Wellness Crossroads seeks to help you with disability and illness related concerns and training needs. We provide nutritional counseling services to people with and without disabilities throughout the lifespan. Offering disability consulting, body image coaching and accessible recreation consultation.</p>
    <svg class="photo-area" viewBox="0 0 290 410" aria-hidden="true">
      <defs>
        <linearGradient id="photoCoach" x1="0" y1="0" x2="1" y2="1">
          <stop offset="0" stop-color="#e9b9a2"/><stop offset="1" stop-color="#8f7a6a"/>
        </linearGradient>
        <linearGradient id="photoKids" x1="0" y1="0" x2="1" y2="1">
          <stop offset="0" stop-color="#b07a55"/><stop offset=".6" stop-color="#6d5a4c"/><stop offset="1" stop-color="#3f4f63"/>
        </linearGradient>
      </defs>
      <path d="M70 210 C120 180 200 175 290 190 L290 410 L80 410 Z" fill="#1f8a70"/>
      <path d="M80 214 C130 188 200 184 282 198 L282 290 L100 245 Z" fill="url(#photoCoach)"/>
      <path d="M96 252 L282 300 L282 404 L110 404 C90 350 90 300 96 252 Z" fill="url(#photoKids)"/>
    </svg>
    <div class="fill" role="img" aria-label="Photo of a woman coaching a young girl at a table" style="left:140px;top:200px;width:1px;height:1px"></div>
    <div class="fill" role="img" aria-label="Photo of cheering children playing bowling indoors" style="left:180px;top:340px;width:1px;height:1px"></div>
    <div class="badge badge--purple"></div>
    <div class="badge badge--grey"></div>
    <div class="badge badge--pink"></div>
  </article>
</section>

</body>
</html>
```